Corporate Design für fenno-atelier
Zielgruppe
personalisierbare bedruckte Artikel
Geschenkverpackung
Designprodukte
papierdesign
Zielgruppe moderne Junge Menschen 20-40 Jahre, mit und ohne Kindern, aktiv in Leben, eher Stadtbewohner
Aufgabenstellung
Das design muss universell einsetzbar sein, soll cool, modern aber trotzdem etwas verspielt sein. Soll für Kinderkollektion und Erwachsenen Kollektion geeignet sein. Die Marke fenno-atelier muss nicht unbediengt ganz groß ausgeschrieben sein.Alle unsere Artikel sind z. B. bei kaufora zu finden, bitte bei der Suche fenno-atelier eintragen.

```html
<!DOCTYPE html>
<html lang="de">
<head>
<meta charset="utf-8">
<title>fenno-atelier – Geschäftsausstattung</title>
<link rel="stylesheet" href="https://fonts.googleapis.com/css2?family=Roboto:ital,wght@0,400;0,700;1,700&display=swap">
<style>
  :root {
    --bg-top: #a9b2dc;
    --bg-bottom: #e3e1ef;
    --brand-blue: #8794c4;
    --brand-coral: #e8695e;
    --coral-shade: #d85d53;
    --paper: #f3f1ee;
    --paper-head: #ebe8e4;
    --ink: #1d1d1f;
  }
  * { box-sizing: border-box; margin: 0; padding: 0; }
  html, body { width: 1200px; height: 1054px; overflow: hidden; }
  body {
    position: relative;
    font-family: "Roboto", Arial, sans-serif;
    background: linear-gradient(160deg, var(--bg-top) 0%, var(--bg-bottom) 70%);
    color: var(--ink);
  }

  /* brand lockup: circle + name */
  .lockup { display: flex; align-items: center; gap: 10px; color: var(--brand-blue); font-weight: 700; }
  .lockup .dot { border: 4px solid currentColor; border-radius: 50%; flex: none; }
  .hero-lockup { position: absolute; left: 50px; top: 60px; font-size: 40px; }
  .hero-lockup .dot { width: 64px; height: 64px; border-width: 6px; }

  /* folder */
  .folder {
    position: absolute; left: 40px; top: 270px; width: 520px; height: 380px;
    background: var(--brand-coral); display: grid; grid-template-columns: repeat(4, 1fr);
  }
  .folder .panel { border-right: 1px solid rgba(0,0,0,.08); }
  .folder .panel:nth-child(2) { background: var(--coral-shade); }
  .folder .panel:last-child { border-right: 0; }

  /* letterhead */
  .letterhead {
    position: absolute; left: 600px; top: 50px; width: 540px; height: 764px;
    background: var(--paper); border: 4px solid var(--brand-blue);
    display: flex; flex-direction: column;
  }
  .letterhead .head { background: var(--paper-head); height: 200px; position: relative; padding: 24px 30px; }
  .letterhead .head .lockup { justify-content: center; font-size: 18px; }
  .letterhead .head .lockup .dot { width: 26px; height: 26px; border-width: 3px; }
  .contact { text-align: center; font-weight: 700; font-style: italic; font-size: 11px; line-height: 1.35; margin-top: 12px; }
  .sender { position: absolute; left: 30px; bottom: 18px; font-weight: 700; font-style: italic; font-size: 10px; line-height: 1.35; }
  .letterhead .body { padding: 20px 30px; flex: 1; position: relative; }
  .greeting { color: var(--brand-coral); font-weight: 700; font-size: 34px; margin-bottom: 12px; }
  .copy { font-weight: 700; font-style: italic; font-size: 11px; line-height: 1.4; text-align: justify; max-width: 470px; }
  .footer-line { position: absolute; right: 30px; bottom: 18px; color: var(--brand-coral); font-weight: 700; font-style: italic; font-size: 10px; }

  /* envelope */
  .envelope { position: absolute; left: 70px; top: 700px; width: 420px; height: 250px; background: #eeedec; }
  .envelope .flap { position: absolute; left: 0; top: 0; width: 100%; height: 70px; background: var(--brand-coral); }
  .envelope .lockup { position: absolute; left: 0; right: 0; top: 110px; justify-content: center; font-size: 16px; }
  .envelope .lockup .dot { width: 22px; height: 22px; border-width: 3px; }

  /* business cards */
  .card { position: absolute; top: 850px; width: 270px; height: 170px; }
  .card-front { left: 530px; background: var(--brand-blue); display: flex; align-items: center; justify-content: center; }
  .card-front .lockup { color: var(--paper); font-size: 24px; }
  .card-front .lockup .dot { width: 40px; height: 40px; }
  .card-back { left: 840px; background: var(--paper); border: 3px solid var(--brand-blue); overflow: hidden; }
  .card-back svg { position: absolute; left: 0; top: 0; }
  .card-back .details { position: absolute; left: 12px; top: 54px; color: var(--paper); font-weight: 700; font-style: italic; font-size: 10px; line-height: 1.4; }
  .card-back .person { position: absolute; right: 16px; top: 60px; text-align: right; color: var(--brand-coral); font-weight: 700; font-size: 14px; line-height: 1.25; }
  .card-back .lockup { position: absolute; right: 16px; top: 20px; font-size: 12px; gap: 6px; }
  .card-back .lockup .dot { width: 16px; height: 16px; border-width: 2px; }
</style>
</head>
<body>

  <div class="lockup hero-lockup"><span class="dot"></span>fenno-atelier</div>

  <div class="folder" aria-label="Mappe">
    <div class="panel"></div><div class="panel"></div><div class="panel"></div><div class="panel"></div>
  </div>

  <article class="letterhead">
    <header class="head">
      <div class="lockup"><span class="dot"></span>fenno-atelier</div>
      <p class="contact">0049 301 772 9<br>www.fenno-atelier.example<br>hallo@fenno-atelier.example</p>
      <p class="sender">adresse<br>beispieltext<br>beispieladresse</p>
    </header>
    <section class="body">
      <h1 class="greeting">hallo!</h1>
      <p class="copy">Lorem ipsum dolor sit amet, consectetur adipisicing elit, sed do eiusmod tempor incididunt ut labore et dolore magna aliqua. Ut enim ad minim veniam, quis nostrud exercitation ullamco laboris nisi ut aliquip ex ea commodo consequat. Duis aute irure dolor in reprehenderit in voluptate velit esse cillum dolore eu fugiat nulla pariatur. Excepteur sint occaecat cupidatat non proident, sunt in culpa qui officia deserunt mollit anim id est laborum. Sed ut perspiciatis unde omnis iste natus error sit voluptatem accusantium doloremque laudantium, totam rem aperiam, eaque ipsa quae ab illo inventore veritatis et quasi architecto beatae vitae dicta sunt explicabo. Nemo enim ipsam voluptatem quia voluptas sit aspernatur aut odit aut fugit, sed quia consequuntur magni dolores eos qui ratione voluptatem sequi nesciunt. Neque porro quisquam est, qui dolorem ipsum quia dolor sit amet, consectetur, adipisci velit, sed quia non numquam eius modi tempora incidunt ut labore et dolore magnam aliquam quaerat voluptatem.</p>
      <p class="footer-line">beispieltext / adresszusatz / infos</p>
    </section>
  </article>

  <div class="envelope">
    <div class="flap"></div>
    <div class="lockup"><span class="dot"></span>fenno-atelier</div>
  </div>

  <div class="card card-front">
    <div class="lockup"><span class="dot"></span>fenno-atelier</div>
  </div>

  <div class="card card-back">
    <svg width="270" height="170" viewBox="0 0 270 170" aria-hidden="true">
      <path d="M0 -10 A120 95 0 0 1 0 180 Z" fill="#8794c4"/>
      <path d="M0 -10 A125 98 0 0 1 0 180" fill="none" stroke="#e8695e" stroke-width="5"/>
    </svg>
    <p class="details">adresse<br>beispieltext<br>0049 301 772 9<br>lina@fenno.example</p>
    <div class="lockup"><span class="dot"></span>fenno-atelier</div>
    <p class="person">lina sommerfeld<br>beispieltext</p>
  </div>

</body>
</html>
```